Financial Advisor / Asset Manager Wix Design

I'm currently hosting with Wix and my first attempt at a website is live at www.bramwellhollowgroup.com Clearly I am not a web designer and I need help making this more catchy, modern, cross-platform compatible, search engine optimized, etc. I've got logos, hex color pallets, and a slew of other graphics. I'm interested in working with a winning designer to write/refine my copy/language to complete the build.

Full set of graphics https://albums.picnestly.io/r83Kd27WQfa5T1mZC do NOT use the CONSULTING graphics as this is for a related business / different website

Target Market(s)

Individuals, small institutions, endowments, non-profits seeking financial advice and asset / portfolio management

Industry/Entity Type

Financial Services

Coding

Coded - Design and coding required

Font styles to use
Other font styles liked:
• AvenirLTStd - Black, Book, and Roman as appropriate

Requirements
Must have
• Complete, cross platform website integrating my existing logo
Nice to have
• Easy to update format for go-forward maintenance

```html
<!DOCTYPE html>
<html lang="en">
<head>
<meta charset="utf-8">
<title>Bramwell Hollow Group</title>
<link rel="stylesheet" href="https://fonts.googleapis.com/css2?family=Nunito+Sans:wght@300;400;600;700;800;900&display=swap">
<style>
:root{
  --blue:#1c5cb4;
  --blue-deep:#124a9c;
  --blue-bright:#1976d2;
  --ink:#1f2a36;
  --muted:#4a5562;
  --line:#dfe4ea;
  --white:#ffffff;
  --sky-top:#4e77b8;
  --sky-mid:#9fb6d6;
  --dusk:#c98a6a;
}
*{box-sizing:border-box;margin:0;padding:0}
html,body{width:1200px;height:4307px;overflow:hidden}
body{font-family:"Nunito Sans",sans-serif;color:var(--ink);background:var(--white);position:relative}
.abs{position:absolute}
a{color:inherit;text-decoration:none}

/* hero */
.hero{position:absolute;left:0;top:0;width:1200px;height:719px;
  background:linear-gradient(180deg,var(--sky-top) 0%,#6f8fc4 30%,var(--sky-mid) 55%,#d9e2ee 68%,#5d6f8a 85%,#2e3c52 100%)}
.brand{display:flex;align-items:center;gap:12px;color:var(--white);font-weight:600;font-size:22px;letter-spacing:1px}
.brand-mark{width:26px;height:26px;border:2px solid var(--white)}
.nav{position:absolute;top:24px;left:520px;display:flex;gap:0;color:var(--white);font-size:14px;font-weight:600}
.nav a{position:absolute;white-space:nowrap}
.nav .sep{position:absolute;width:1px;height:14px;background:rgba(255,255,255,.7);top:3px}
.nav .active{border-bottom:2px solid var(--white);padding-bottom:6px}
.hero-title{color:var(--white);font-size:36px;line-height:44px;text-shadow:0 2px 6px rgba(0,0,0,.25)}
.hero-title b{font-weight:900;display:block}
.hero-title span{font-weight:300;display:block}
.dots{left:552px;top:672px;display:flex;gap:15px}
.dots i{width:13px;height:13px;border:2px solid var(--white);border-radius:50%}
.dots i.on{background:var(--white)}

.section-title{position:absolute;left:0;width:1200px;text-align:center;font-weight:300;font-size:40px;letter-spacing:.5px;color:var(--ink)}
.section-title::after{content:"";display:block;width:74px;height:3px;background:var(--blue-bright);margin:12px auto 0}

/* hexes */
.hex{position:absolute;width:244px;height:280px;clip-path:polygon(50% 0,100% 25%,100% 75%,50% 100%,0 75%,0 25%);color:var(--white);text-align:center;padding:0 16px}
.hex.dark{background:linear-gradient(160deg,#3a3f46,#14171b)}
.hex.blue{background:linear-gradient(160deg,#2f7fd6,#1556a8)}
.hex .ico{width:56px;height:56px;margin:62px auto 18px;display:block}
.hex h3{font-size:17px;font-weight:800;margin-bottom:6px}
.hex p{font-size:12.5px;line-height:25px}

/* who */
.who{position:absolute;left:0;top:1170px;width:1200px;height:576px;background:linear-gradient(180deg,#f7f8fa,#eef1f4)}
.who h2{position:absolute;left:100px;top:108px;font-size:46px;font-weight:300}
.who h2::after{content:"";display:block;width:72px;height:3px;background:var(--blue-bright);margin-top:2px}
.who p{position:absolute;left:100px;top:190px;width:450px;font-size:14px;line-height:32px;color:var(--muted);text-align:justify}
.btn{position:absolute;background:linear-gradient(180deg,#1f86e0,#1460b8);color:var(--white);font-weight:800;font-size:15px;display:flex;align-items:center;justify-content:center;border-radius:3px}
.portrait{position:absolute;left:622px;top:50px;width:468px;height:468px;border-radius:50%;border:6px solid var(--blue-deep);background:radial-gradient(circle at 50% 40%,#c9a98c,#7d6a4f 55%,#3c4a3a)}

/* offer */
.offer{position:absolute;left:0;top:1746px;width:1200px;height:577px;background:linear-gradient(180deg,#1d5db5,#1a55a9 60%,#2a63b0)}
.offer .section-title{color:var(--white);top:82px}
.card{position:absolute;width:238px;height:268px;border:1px solid rgba(255,255,255,.6);border-radius:4px;text-align:center;color:var(--white);padding:0 16px}
.card.hi{background:var(--white);color:var(--ink);border-color:var(--white)}
.card .ico{width:50px;height:50px;margin:30px auto 14px;display:block}
.card h3{font-size:17px;font-weight:800;margin-bottom:8px}
.card p{font-size:12px;line-height:21px}
.card a{display:inline-block;margin-top:10px;font-weight:800;font-size:14.5px;text-decoration:underline}
.card.hi a{color:var(--blue)}

/* faq */
.faq{position:absolute;left:155px;width:891px;height:60px;background:var(--white);box-shadow:0 2px 8px rgba(0,0,0,.12);display:flex;align-items:center;padding-left:26px;font-size:20px;color:#2c3540}
.faq .plus{position:absolute;right:6px;top:6px;width:58px;height:48px;background:var(--blue);}
.faq .plus::before,.faq .plus::after{content:"";position:absolute;background:var(--white);left:50%;top:50%;transform:translate(-50%,-50%)}
.faq .plus::before{width:24px;height:2px}
.faq .plus::after{width:2px;height:24px}

/* contact */
.contact-bg{position:absolute;left:0;top:3426px;width:1200px;height:451px;background:linear-gradient(180deg,#ffffff 0%,#e8c9b6 25%,var(--dusk) 55%,#7a5a66 80%,#3c3b45 100%)}
.info h4{font-size:18px;font-weight:800;color:var(--ink);margin-bottom:6px}
.info p{font-size:15px;line-height:23px;color:var(--muted)}
.social{display:flex;gap:13px}
.social i{width:42px;height:42px;border-radius:50%;background:var(--blue);border:2px solid #cfdcf0}
.form{position:absolute;left:510px;top:3259px;width:530px;height:407px;background:var(--white);box-shadow:0 4px 20px rgba(0,0,0,.1);padding:34px 38px}
.form h4{font-size:18px;font-weight:800;margin-bottom:22px}
.field{position:relative;border-bottom:1px solid var(--line);height:72px;font-size:15px;color:#444;padding-top:14px}
.field svg{position:absolute;right:6px;top:14px}

/* footer */
.footer{position:absolute;left:0;top:3877px;width:1200px;height:430px;background:linear-gradient(180deg,#1a56ad,#14499b)}
.footer .col{position:absolute;color:var(--white)}
.footer h5{font-size:16px;font-weight:700;margin-bottom:14px}
.footer li{list-style:none;font-size:14px;line-height:33px}
.footer .vr{position:absolute;width:2px;height:30px;background:var(--white);top:120px}
.footer .social i{width:40px;height:40px;background:transparent;border:2px solid rgba(255,255,255,.8)}
.copy{position:absolute;left:100px;right:100px;top:4258px;display:flex;justify-content:space-between;color:var(--white);font-size:14px}
.fline{position:absolute;left:100px;width:1000px;height:1px;background:rgba(255,255,255,.3);top:4225px}
</style>
</head>
<body>

<section class="hero" role="img" aria-label="Snow-capped mountain range under a blue sky with low clouds">
</section>
<div class="abs brand" style="left:100px;top:22px"><span class="brand-mark"></span>BRAMWELL HOLLOW GROUP</div>
<nav class="nav">
  <a class="active" style="left:0">HOME</a>
  <span class="sep" style="left:80px"></span>
  <a style="left:120px">ABOUT</a>
  <span class="sep" style="left:206px"></span>
  <a style="left:245px">FAQS</a>
  <span class="sep" style="left:318px"></span>
  <a style="left:359px">SERVICES ▾</a>
  <span class="sep" style="left:473px"></span>
  <a style="left:511px">CONTACT</a>
</nav>
<div class="abs hero-title" style="left:97px;top:152px"><b>Personalized financial advice</b><span>to help you achieve your goals</span></div>
<div class="abs hero-title" style="right:97px;top:568px;text-align:right"><b>Professional management</b><span>to make your money work for you</span></div>
<div class="abs dots"><i></i><i class="on"></i><i></i><i></i></div>

<h2 class="section-title" style="top:800px">WHY WORK WITH US</h2>

<div class="hex dark" style="left:100px;top:886px">
  <svg class="ico" viewBox="0 0 56 56" fill="none" stroke="#fff" stroke-width="2"><path d="M8 30l10-10 10 6 10-6 10 10-14 12-6-4-6 4z"/></svg>
  <h3>You Come First</h3><p>We always act in the best interests of our clients</p>
</div>
<div class="hex blue" style="left:353px;top:886px">
  <svg class="ico" viewBox="0 0 56 56" fill="none" stroke="#fff" stroke-width="2"><circle cx="28" cy="28" r="20"/><circle cx="28" cy="24" r="6"/><path d="M18 40c2-6 18-6 20 0"/></svg>
  <h3>Personalized Services</h3><p>We get to know you in order to service your unique needs</p>
</div>
<div class="hex dark" style="left:605px;top:886px">
  <svg class="ico" viewBox="0 0 56 56" fill="none" stroke="#fff" stroke-width="2"><circle cx="32" cy="16" r="9"/><path d="M8 40h12l10 4 16-10"/></svg>
  <h3>Transparent Fees</h3><p>You'll always know what you pay and how we get paid</p>
</div>
<div class="hex dark" style="left:857px;top:886px">
  <svg class="ico" viewBox="0 0 56 56" fill="none" stroke="#fff" stroke-width="2"><path d="M30 10l10 8-10 8"/><path d="M8 40h12l10 4 16-10"/></svg>
  <h3>We Give Back</h3><p>We support and better our local communities</p>
</div>

<section class="who">
  <h2>WHO WE ARE</h2>
  <p>Bramwell Hollow Group is a registered investment advisory firm committed to serving as fiduciary to our clients. We always act in the best interests of our clients, including putting your interests ahead of our own. We provide independent financial planning, investment management, and asset management services tailored to your unique needs &amp; circumstances.</p>
  <a class="btn" style="left:100px;top:401px;width:152px;height:44px">LEARN MORE</a>
  <div class="portrait" role="img" aria-label="Portrait photo of the firm's advisor"></div>
</section>

<section class="offer">
  <h2 class="section-title">WHAT WE OFFER</h2>
  <div class="card" style="left:100px;top:219px">
    <svg class="ico" viewBox="0 0 50 50" fill="none" stroke="#fff" stroke-width="2"><rect x="8" y="6" width="26" height="34"/><rect x="26" y="26" width="18" height="18"/></svg>
    <h3>Financial Planning</h3><p>You and your circumstances are unique. We want to work to meet you where you are today,</p><a>LEARN MORE</a>
  </div>
  <div class="card hi" style="left:353px;top:187px">
    <svg class="ico" viewBox="0 0 50 50" fill="none" stroke="#1c5cb4" stroke-width="2"><circle cx="25" cy="25" r="18"/><path d="M18 32V24M25 32V18M32 32V22"/></svg>
    <h3>Asset Management</h3><p>Many advisors use a screening process to find investments. You may be familiar</p><a>LEARN MORE</a>
  </div>
  <div class="card" style="left:607px;top:219px">
    <svg class="ico" viewBox="0 0 50 50" fill="none" stroke="#fff" stroke-width="2"><path d="M10 44V30M18 44V24M26 44V18M34 44V26"/><circle cx="36" cy="12" r="6"/></svg>
    <h3>Portfolio Optimization</h3><p>Your investment portfolio was built with money you earned. It should be customized</p><a>LEARN MORE</a>
  </div>
  <div class="card" style="left:859px;top:187px">
    <svg class="ico" viewBox="0 0 50 50" fill="none" stroke="#fff" stroke-width="2"><circle cx="16" cy="12" r="6"/><circle cx="34" cy="12" r="6"/><circle cx="14" cy="34" r="4"/><circle cx="25" cy="34" r="4"/><circle cx="36" cy="34" r="4"/></svg>
    <h3>Alternative Investments</h3><p>The challenges facing investors seeking to build portfolios capable of generating</p><a>LEARN MORE</a>
  </div>
</section>

<h2 class="section-title" style="top:2408px">FREQUENTLY ASKED QUESTIONS</h2>
<div class="faq" style="top:2510px">What is a registered investment advisor? Are you a registered investment advisor?<span class="plus"></span></div>
<div class="faq" style="top:2597px">What does being an independent financial advisor mean? Why does it matter?<span class="plus"></span></div>
<div class="faq" style="top:2685px">What is a fiduciary? Are you a fiduciary?<span class="plus"></span></div>
<div class="faq" style="top:2772px">What is a fiduciary? Are you a fiduciary?<span class="plus"></span></div>
<div class="faq" style="top:2860px">What is a custodian? Are you a custodian?<span class="plus"></span></div>
<div class="faq" style="top:2948px">What are your fees? How much will I pay?<span class="plus"></span></div>

<h2 class="section-title" style="top:3110px">GET IN TOUCH</h2>
<p class="abs" style="left:0;width:1200px;top:3178px;text-align:center;font-size:15px;line-height:24px;color:var(--muted)">At vero eos et accusamus et iustignissimos ducimus qui blanditiis praesentium<br>voluptatum deleniti atque corrupti quos dolores</p>

<div class="contact-bg" role="img" aria-label="Mountain range glowing orange at sunset above a pine forest"></div>

<div class="abs info" style="left:159px;top:3288px">
  <h4>LOCATION:</h4><p>2860 Larkfield Rd, Suite #204<br>Ashby Vale, VA 24410</p>
</div>
<div class="abs info" style="left:159px;top:3394px">
  <h4>EMAIL ADDRESS:</h4><p>info@bramwellhollowgroup.com</p>
</div>
<div class="abs info" style="left:159px;top:3478px">
  <h4>CALL US NOW:</h4><p>(555) 201-3384</p>
</div>
<div class="abs info" style="left:159px;top:3561px">
  <h4>FOLLOW NOW:</h4>
  <div class="social" aria-label="Social links"><i></i><i></i><i></i><i></i></div>
</div>

<form class="form">
  <h4>DROP YOUR MESSAGE</h4>
  <div class="field">Jonathan Doe<svg width="20" height="20" viewBox="0 0 20 20" fill="none" stroke="#666" stroke-width="1.4"><circle cx="10" cy="7" r="4"/><path d="M3 18c1-5 13-5 14 0"/></svg></div>
  <div class="field">Email Address<svg width="20" height="20" viewBox="0 0 20 20" fill="none" stroke="#666" stroke-width="1.4"><rect x="2" y="5" width="16" height="11"/><path d="M2 5l8 6 8-6"/></svg></div>
  <div class="field" style="height:110px">Message<svg width="24" height="22" viewBox="0 0 24 22" fill="none" stroke="#666" stroke-width="1.4"><ellipse cx="12" cy="10" rx="10" ry="7"/><path d="M6 16l-2 4 6-3"/></svg></div>
  <a class="btn" style="left:252px;top:326px;width:244px;height:48px">CONTACT US NOW</a>
</form>

<footer class="footer">
  <div class="col" style="left:104px;top:105px"><div class="brand" style="font-size:20px"><span class="brand-mark"></span>BRAMWELL HOLLOW</div></div>
  <div class="col social" style="left:118px;top:172px"><i></i><i></i><i></i><i></i></div>
  <span class="vr" style="left:398px"></span>
  <div class="col" style="left:465px;top:84px"><h5>Quick Link</h5><ul><li>Home</li><li>About</li><li>FAQs</li><li>Services</li><li>Contact</li></ul></div>
  <span class="vr" style="left:611px"></span>
  <div class="col" style="left:677px;top:84px"><h5>Other Link</h5><ul><li>Who We Are</li><li>Career</li><li>News</li><li>Resources</li><li>Contact</li></ul></div>
  <span class="vr" style="left:823px"></span>
  <div class="col" style="left:891px;top:84px;font-size:14px;line-height:22px">
    <h5>Contact Info</h5>
    <p>&#9679; 2860 Larkfield Rd, Suite #204<br>&nbsp;&nbsp;&nbsp;Ashby Vale, VA 24410</p>
    <p style="margin-top:14px">&#9742; (555) 201-3384</p>
    <p style="margin-top:14px">&#9993; info@bramwellhollowgroup.com</p>
  </div>
</footer>
<div class="fline"></div>
<div class="copy"><span>Copyright © 2022 - Bramwell Hollow Group. All Right Reserved</span><span>Privacy Policy &nbsp;|&nbsp; Terms &amp; Conditions</span></div>

</body>
</html>
```